business cards and stationary for landscaping company
Seven Hollows Lawn and Landscaping
business cards and stationary for landscaping company - Home and Garden
Creative Brief
Use specific fonts
Feel free to change fonts
Simple
Desmond Kuparik
2817 Mellard Rd. Brockville ON K2p4v8
Desmond@kuparik-mail.example
7HollowsLL.example
On the front of the cards we would like it to be simple and clean with just the logo. Personal name and number. We need it in a format so we can change all of the contact information for the other owners of the company so make sure we will be able to do that with the design submissions. We are not looking for anything to crazy in terms of the design so pleas NO see thru cards that iv seen on here before or anything that will cost extra to have printed. We would like to see the face of the cards on White Green and Black there are three owners so we would like each to have a different card face. I will attach some samples of the front of the cards and colors we liked. We don't need an address on the card We would also like the same design as business card in a larger format to put on postcards plus maybe the addition of a picture of some of our work we have done. i will attach some pictures as well for the postcards.
On the Back of the cards we would like to include our services and once more all our contact information including name number email and website domain Landscaping - Patio Design and Insulation and Repair - Walkway Design and Insulation - Garden and Driveway Edging - & More Property Maintenance - Lawn Care - Brush Cutting - Yard Cleanup & More Please remember to make the text able to be edited. so we are able to make changes if necessary.

```html
<!DOCTYPE html>
<html lang="en">
<head>
<meta charset="utf-8">
<title>Seven Hollows Lawn and Landscaping – Stationery</title>
<link href="https://fonts.googleapis.com/css2?family=Montserrat:wght@400;600;700&display=swap" rel="stylesheet">
<style>
  :root{
    --green:#1e8c3c;
    --green-dark:#14652a;
    --charcoal:#333536;
    --paper:#ffffff;
    --ink:#4a4a4a;
    --muted:#9a9a9a;
    --stage-light:#a9abab;
    --stage-dark:#5b5d5e;
  }
  *{box-sizing:border-box;margin:0;padding:0}
  html,body{width:1200px;height:247px;overflow:hidden}
  body{font-family:"Montserrat",sans-serif;color:var(--ink)}
  .stage{position:relative;width:1200px;height:247px;
    background:radial-gradient(ellipse at 50% 40%,var(--stage-light),var(--stage-dark) 85%)}
  .piece{position:absolute;box-shadow:0 1px 3px rgba(0,0,0,.45);overflow:hidden;background:var(--paper)}
  .brand{display:flex;align-items:center;gap:.4em;font-weight:700;color:var(--green);line-height:1;white-space:nowrap}
  .brand .mark{width:1.6em;height:1.6em;background:currentColor;flex:none}
  .brand .name{text-transform:uppercase;letter-spacing:.04em}
  .brand .name small{display:block;font-size:.45em;font-weight:700;letter-spacing:.08em;margin-top:.25em}
  .brand.light{color:var(--paper)}
  .centered{position:absolute;inset:0;display:flex;align-items:center;justify-content:center}
  .contact{font-size:3px;line-height:1.5;color:var(--ink);white-space:nowrap}
  .contact.light{color:var(--paper)}
  .contact b{font-weight:700;font-size:1.3em;display:block}

  .card-dark{background:var(--charcoal)}
  .card-green{background:var(--green)}
  .stripe-left{position:absolute;left:0;top:0;bottom:0;width:5px;background:var(--green)}
  .stripe-bottom{position:absolute;left:0;right:0;bottom:0;height:4px;background:var(--green)}

  .letter{padding:12px 9px}
  .letter .brand{font-size:5px}
  .letter .body{margin-top:16px;font-size:2.6px;line-height:1.7;color:var(--muted)}
  .letter .sign{margin-top:8px;font-size:2.6px;color:var(--ink)}
  .letter .foot{position:absolute;left:0;right:0;bottom:0;height:12px;background:var(--green);
    color:var(--paper);font-size:2.2px;display:flex;align-items:center;justify-content:center;gap:5px;white-space:nowrap}

  .env-flap{position:absolute;left:0;right:0;top:0;height:45%;background:var(--green-dark)}
  .env-green{background:var(--green)}

  .folder{display:flex;background:transparent}
  .folder .panel{width:50%;height:100%;position:relative}
  .folder .inside{background:var(--paper)}
  .folder .inside .band{position:absolute;left:0;right:0;bottom:0;height:26%;background:var(--green)}
  .folder .inside .contact{position:absolute;left:12px;top:24px;font-size:4px}
  .folder .cover{background:var(--green)}
  .folder .cover .tag{position:absolute;left:0;right:0;bottom:22px;text-align:center;color:var(--paper);font-size:4px;letter-spacing:.1em}
</style>
</head>
<body>
<main class="stage">

  <section class="piece card-dark" style="left:12px;top:98px;width:124px;height:64px">
    <div class="centered"><div class="brand" style="font-size:7px"><span class="mark"></span><span class="name">Seven Hollows<small>Lawn and Landscaping</small></span></div></div>
  </section>

  <section class="piece" style="left:12px;top:172px;width:58px;height:33px">
    <div class="stripe-left"></div>
    <div class="contact" style="position:absolute;left:9px;top:8px"><b>Desmond Kuparik</b>613-555-0147<br>7HollowsLL.example</div>
  </section>
  <section class="piece card-green" style="left:74px;top:172px;width:58px;height:33px">
    <div class="centered"><div class="brand light" style="font-size:4px"><span class="mark"></span><span class="name">Seven Hollows</span></div></div>
  </section>
  <section class="piece card-dark" style="left:12px;top:209px;width:58px;height:33px">
    <div class="centered"><div class="brand" style="font-size:4px"><span class="mark"></span><span class="name">Seven Hollows</span></div></div>
  </section>
  <section class="piece card-green" style="left:74px;top:209px;width:58px;height:33px">
    <div class="contact light" style="position:absolute;left:5px;top:9px;font-size:2.6px"><b>Desmond Kuparik</b>613-555-0147<br>Desmond@kuparik-mail.example</div>
  </section>

  <section class="piece" style="left:140px;top:172px;width:96px;height:50px">
    <div class="brand" style="position:absolute;left:8px;top:10px;font-size:5px"><span class="mark"></span><span class="name">Seven Hollows<small>Lawn and Landscaping</small></span></div>
    <div class="stripe-bottom" style="height:7px"></div>
  </section>

  <article class="piece letter" style="left:246px;top:28px;width:96px;height:210px">
    <div class="brand"><span class="mark"></span><span class="name">Seven Hollows<small>Lawn and Landscaping</small></span></div>
    <p class="body">Thank you for choosing our team for your lawn and garden work this season. We look forward to serving you.</p>
    <p class="sign">Sincerely,<br>Desmond Kuparik</p>
    <div class="foot"><span>2817 Mellard Rd. Brockville ON K2p4v8</span><span>7HollowsLL.example</span></div>
  </article>
  <article class="piece letter" style="left:346px;top:28px;width:96px;height:210px">
    <div class="brand"><span class="mark"></span><span class="name">Seven Hollows<small>Lawn and Landscaping</small></span></div>
    <p class="body">Thank you for choosing our team for your lawn and garden work this season. We look forward to serving you.</p>
    <p class="sign">Sincerely,<br>Desmond Kuparik</p>
    <div class="foot"><span>2817 Mellard Rd. Brockville ON K2p4v8</span><span>7HollowsLL.example</span></div>
  </article>

  <section class="piece" style="left:450px;top:72px;width:110px;height:38px">
    <div class="stripe-left" style="width:8px"></div>
    <div class="brand" style="position:absolute;left:16px;top:11px;font-size:5px"><span class="mark"></span><span class="name">Seven Hollows<small>Lawn and Landscaping</small></span></div>
  </section>
  <section class="piece" style="left:450px;top:118px;width:110px;height:34px">
    <div class="contact" style="position:absolute;left:8px;top:8px;font-size:2.6px"><b>Desmond Kuparik</b>613-555-0147 · Desmond@kuparik-mail.example<br>2817 Mellard Rd. Brockville ON K2p4v8</div>
    <div class="stripe-bottom"></div>
  </section>
  <section class="piece card-green" style="left:566px;top:78px;width:62px;height:34px">
    <div class="centered"><div class="brand light" style="font-size:4px"><span class="mark"></span><span class="name">Seven Hollows</span></div></div>
  </section>
  <section class="piece" style="left:566px;top:118px;width:62px;height:34px">
    <div class="centered"><div class="brand" style="font-size:4px"><span class="mark"></span><span class="name">Seven Hollows</span></div></div>
  </section>

  <section class="piece env-green" style="left:572px;top:165px;width:110px;height:36px">
    <div class="env-flap"></div>
  </section>
  <section class="piece card-dark" style="left:692px;top:160px;width:138px;height:42px">
    <div class="env-flap"></div>
    <div class="brand" style="position:absolute;left:8px;bottom:6px;font-size:4px"><span class="mark"></span><span class="name">Seven Hollows</span></div>
  </section>
  <section class="piece" style="left:692px;top:208px;width:138px;height:32px">
    <div class="brand" style="position:absolute;left:8px;top:6px;font-size:4px"><span class="mark"></span><span class="name">Seven Hollows</span></div>
    <div class="contact" style="position:absolute;left:8px;bottom:6px;font-size:2.6px">2817 Mellard Rd. Brockville ON K2p4v8</div>
    <div class="stripe-bottom" style="height:3px"></div>
  </section>

  <section class="piece folder" style="left:840px;top:34px;width:324px;height:196px">
    <div class="panel inside">
      <div class="contact"><b>Desmond Kuparik</b>613-555-0147<br>Desmond@kuparik-mail.example<br>7HollowsLL.example</div>
      <div class="band"></div>
    </div>
    <div class="panel cover">
      <div class="centered"><div class="brand light" style="font-size:11px"><span class="mark"></span><span class="name">Seven Hollows<small>Lawn and Landscaping</small></span></div></div>
      <div class="tag">7HollowsLL.example</div>
    </div>
  </section>

</main>
</body>
</html>
```